Briefpapier für Seehafenspedition im Bereich Zollabfertigung
Zielgruppe
Seehafenspedition im Bereich Zollabfertigung (Import & Export), Hafenabfertigung und weltweiter Transport (See- und Landtransporte). Zielgruppe sind Privatkunden als auch Geschäftskunden.
Aufgabenstellung
Wir bitten um ein Design für unser Briefpapier.
Wir suchen ein hochwertiges Design, das die Werte Vertrauen, Exklusivität und Innovation ausstrahlt. Es soll edel aussehen.
Bitte für Telefon, Mail etc. Icons benutzen, damit es für jedermann verständlich ist, unabhängig von der Sprache.
Bitte orientieren Sie sich am Design unseres Logos und unserer Visitenkarten.
Die Datensätze sollten sich mit entsprechendem Programm von uns bearbeiten lassen.
Wir freuen uns schon auf die Entwürfe.
Vielen Dank im Voraus!

```html
<!DOCTYPE html>
<html lang="de">
<head>
<meta charset="utf-8">
<title>Meridian Cargo – Briefpapier</title>
<link href="https://fonts.googleapis.com/css2?family=Roboto:wght@400;500&display=swap" rel="stylesheet">
<style>
  :root {
    --orange: #f39200;
    --grey: #55575a;
    --line: #9a9a9a;
    --paper: #ffffff;
  }
  * { margin: 0; padding: 0; box-sizing: border-box; }
  html, body { width: 867px; height: 1200px; overflow: hidden; background: var(--paper); }
  body { position: relative; font-family: "Roboto", Arial, sans-serif; color: var(--grey); }

  .top-band { position: absolute; left: 0; top: 0; width: 867px; height: 15px; background: var(--orange); }

  .brand { position: absolute; left: 567px; top: 60px; display: flex; align-items: center; gap: 8px; }
  .brand-dot { width: 34px; height: 34px; border-radius: 50%; background: var(--orange); }
  .brand-name { font-size: 22px; font-weight: 500; letter-spacing: 3px; color: var(--grey); line-height: 1.05; }

  .contact { position: absolute; left: 620px; top: 114px; font-size: 10.5px; line-height: 13px; }
  .contact-rule { position: absolute; left: 0; top: 18px; width: 1px; height: 181px; background: var(--line); }
  .contact-marker { position: absolute; left: -2px; top: 3px; }
  .contact-body { padding-left: 9px; }
  .company { font-size: 13px; line-height: 16px; font-weight: 400; }
  .group { margin-top: 10px; }
  .group-title { color: var(--orange); }
  .icon-row { display: flex; align-items: center; gap: 4px; font-size: 11px; line-height: 16px; }

  .return-address { position: absolute; left: 136px; top: 183px; width: 248px; font-size: 8.5px;
    padding-bottom: 3px; border-bottom: 1px solid var(--line); white-space: nowrap; }
  .return-address .sep { color: var(--orange); }

  .fold-mark { position: absolute; left: 5px; }

  .footer-band { position: absolute; left: 0; top: 1174px; }
  .website { position: absolute; left: 0; top: 1177px; width: 838px; text-align: center;
    color: #fff; font-size: 14px; font-weight: 500; display: flex; justify-content: center; align-items: center; gap: 6px; }
</style>
</head>
<body>
  <div class="top-band"></div>

  <div class="brand">
    <span class="brand-dot"></span>
    <span class="brand-name">MERIDIAN<br>CARGO</span>
  </div>

  <div class="contact">
    <svg class="contact-marker" width="5" height="8" viewBox="0 0 5 8"><polygon points="0,0 5,4 0,8" fill="var(--orange)"/></svg>
    <div class="contact-rule"></div>
    <div class="contact-body">
      <div class="company">Meridian Cargo GmbH</div>
      <div>Kaistraße 9</div>
      <div>27568 Bremerhaven</div>

      <div class="group">
        <div class="icon-row">
          <svg width="10" height="10" viewBox="0 0 24 24"><path fill="var(--orange)" d="M6.6 10.8c1.4 2.8 3.8 5.1 6.6 6.6l2.2-2.2c.3-.3.7-.4 1-.2 1.1.4 2.3.6 3.6.6.6 0 1 .4 1 1V20c0 .6-.4 1-1 1C10.6 21 3 13.4 3 4c0-.6.4-1 1-1h3.5c.6 0 1 .4 1 1 0 1.3.2 2.5.6 3.6.1.3 0 .7-.2 1z"/></svg>
          <span>+49 471 5550312-0</span>
        </div>
        <div class="icon-row">
          <svg width="10" height="10" viewBox="0 0 24 24"><path fill="var(--orange)" d="M2 5h20v14H2z"/><path fill="none" stroke="#fff" stroke-width="2" d="M2 5l10 8 10-8"/></svg>
          <span>info@meridiancargo.de</span>
        </div>
      </div>

      <div class="group">
        <div class="group-title">Bremerhaven:</div>
        <div>Register: HRB 40817 HB;</div>
        <div>USt-IdNr. / VAT-No.: DE123456789;</div>
        <div>Geschäftsführer / CEO: Henrik Albers</div>
      </div>

      <div class="group">
        <div class="group-title">Hansebank</div>
        <div>IBAN: DE00 1234 5678 9012 3456 78</div>
        <div>BIC: HNSBDEHBXXX</div>
      </div>
    </div>
  </div>

  <div class="return-address">Meridian Cargo GmbH <span class="sep">|</span> Kaistraße 9 <span class="sep">|</span> 27568 Bremerhaven</div>

  <svg class="fold-mark" style="top:400px" width="5" height="8" viewBox="0 0 5 8"><polygon points="0,0 5,4 0,8" fill="var(--orange)"/></svg>
  <svg class="fold-mark" style="top:804px" width="5" height="8" viewBox="0 0 5 8"><polygon points="0,0 5,4 0,8" fill="var(--orange)"/></svg>

  <svg class="footer-band" width="867" height="26" viewBox="0 0 867 26">
    <polygon points="0,0 664,0 677,7 842,7 811,26 0,26" fill="var(--orange)"/>
  </svg>
  <div class="website">
    <svg width="14" height="14" viewBox="0 0 24 24" fill="none" stroke="#fff" stroke-width="2">
      <circle cx="12" cy="12" r="10"/><ellipse cx="12" cy="12" rx="4.5" ry="10"/><path d="M2 12h20M4 7h16M4 17h16"/>
    </svg>
    <span>www.meridiancargo.de</span>
  </div>
</body>
</html>
```